Dunmore Acres Enterprise
Home grown grain fed beef Wholes, Halfs, Quarters
Locally raised
No Added Hormones
Call or text now to order (555) -0418-2957

```html
<!DOCTYPE html>
<html lang="en">
<head>
<meta charset="utf-8">
<title>Dunmore Acres Enterprise – Grain-Fed Beef Flyer</title>
<link rel="stylesheet" href="https://fonts.googleapis.com/css2?family=Poppins:wght@400;500;600;700;800&display=swap">
<style>
  :root {
    --page-bg: #e9ece9;
    --flyer-dark: #242424;
    --flyer-green: #1f8a43;
    --accent-lime: #8dc63f;
    --text-white: #ffffff;
    --card-white: #f7f7f7;
    --meat-red: #b83a3e;
    --meat-deep: #8e2a2e;
    --leaf-light: #8fd27a;
    --leaf-deep: #3f9a48;
  }
  * { margin: 0; padding: 0; box-sizing: border-box; }
  html, body { width: 1200px; height: 800px; overflow: hidden; }
  body {
    background: var(--page-bg);
    font-family: "Poppins", sans-serif;
    position: relative;
  }
  .flyer {
    position: absolute;
    left: 340px; top: 32px;
    width: 520px; height: 736px;
    overflow: hidden;
    background:
      radial-gradient(ellipse 420px 360px at 20% 18%, rgba(31,138,67,0.95), rgba(31,138,67,0) 70%),
      radial-gradient(ellipse 300px 260px at 30% 60%, rgba(31,138,67,0.45), rgba(31,138,67,0) 70%),
      var(--flyer-dark);
    color: var(--text-white);
  }
  .leaf-photo {
    position: absolute;
    border-radius: 12px;
    background: linear-gradient(135deg, var(--leaf-light), var(--leaf-deep));
    opacity: 0.85;
  }
  .leaf-photo-top { left: 26px; top: 0; width: 62px; height: 36px; border-radius: 0 0 12px 12px; }
  .leaf-photo-bottom { left: 398px; top: 690px; width: 68px; height: 46px; border-radius: 12px 12px 0 0; }
  .side-dots {
    position: absolute; right: 22px; top: 90px;
    width: 4px; height: 60px;
    background: repeating-linear-gradient(to bottom, #3aa655 0 4px, transparent 4px 14px);
  }
  .brand { position: absolute; left: 120px; right: 20px; top: 56px; text-align: center; }
  .brand-name { font-weight: 800; font-size: 40px; letter-spacing: 1px; line-height: 1.05; }
  .brand-sub { font-weight: 500; font-size: 22px; letter-spacing: 9px; margin-top: 4px; }
  .brand-rule { width: 150px; height: 2px; background: var(--text-white); margin: 12px auto 0; }

  .headline { position: absolute; left: 38px; top: 200px; }
  .headline-line { font-weight: 800; font-size: 34px; line-height: 1.02; text-transform: uppercase; }
  .headline-beef { font-weight: 800; font-size: 84px; line-height: 0.95; color: var(--accent-lime); letter-spacing: 2px; }
  .headline-rule { width: 170px; height: 4px; background: var(--accent-lime); margin-top: 8px; }

  .portions { position: absolute; left: 38px; top: 372px; font-weight: 700; font-size: 18px; line-height: 1.35; text-transform: uppercase; }
  .features { position: absolute; left: 38px; top: 462px; list-style: none; font-size: 14px; font-weight: 500; }
  .features li { display: flex; align-items: center; gap: 10px; margin-bottom: 6px; }
  .features li::before { content: ""; width: 12px; height: 12px; border-radius: 2px; background: var(--accent-lime); }

  .tagline { position: absolute; left: 38px; top: 540px; }
  .tagline-lead { font-weight: 700; font-size: 26px; color: var(--accent-lime); line-height: 1.1; }
  .tagline-rest { font-size: 15px; font-weight: 500; }

  .order-box {
    position: absolute; left: 20px; top: 640px;
    width: 260px; height: 80px;
    border: 1.5px solid var(--accent-lime);
    border-radius: 0 0 18px 0;
    padding: 10px 16px;
  }
  .order-label { font-size: 15px; font-weight: 500; }
  .order-phone { font-size: 24px; font-weight: 700; color: var(--accent-lime); line-height: 1.2; }

  .product-card {
    position: absolute; left: 300px; top: 220px;
    width: 196px; height: 410px;
    background: var(--card-white);
    border-radius: 24px;
    box-shadow: inset 0 0 0 4px var(--card-white), inset 0 0 0 6px var(--accent-lime);
  }
  .product-photo {
    position: absolute; left: 312px; top: 340px;
    width: 172px; height: 200px;
    border-radius: 14px;
    background: linear-gradient(160deg, var(--meat-red), var(--meat-deep));
  }
</style>
</head>
<body>
  <main class="flyer">
    <div class="leaf-photo leaf-photo-top" role="img" aria-label="Photo of a fresh green leaf"></div>
    <div class="leaf-photo leaf-photo-bottom" role="img" aria-label="Photo of a fresh green leaf"></div>
    <div class="side-dots"></div>

    <header class="brand">
      <div class="brand-name">DUNMORE ACRES</div>
      <div class="brand-sub">ENTERPRISE</div>
      <div class="brand-rule"></div>
    </header>

    <section class="headline">
      <div class="headline-line">Homegrow</div>
      <div class="headline-line">Grain-Fed</div>
      <div class="headline-beef">BEEF</div>
      <div class="headline-rule"></div>
    </section>

    <div class="portions">
      <div>Wholes</div>
      <div>Halves</div>
      <div>Quarters Available</div>
    </div>

    <ul class="features">
      <li>Locally Raised</li>
      <li>No Added Hormones</li>
    </ul>

    <div class="tagline">
      <div class="tagline-lead">Fresh, Natural,</div>
      <div class="tagline-rest">and Premium Quality Beef.</div>
    </div>

    <div class="order-box">
      <div class="order-label">Call or Text Now to Order:</div>
      <div class="order-phone">(555) 0418-2957</div>
    </div>

    <div class="product-card"></div>
    <div class="product-photo" role="img" aria-label="Photo of raw beef steaks garnished with fresh rosemary and herbs"></div>
  </main>
</body>
</html>
```